Roofing & Siding door hanger flyer

-Looking to make door hanger flyer for Korvell Roofing & Siding
-4.5" wide x 11" tall
-2 sided full colour
-We have started a new website (the content is changing) I have attached photos.
-About us:
-25 year labour warranty's available
-32 years in Calgary
-QHT A+ Member
-NWPC (Prairie Westmark Shingle Council) (logo attached)
-TEK Summit Premier (logo attached)
-Owen Calloway (logo attached)
-Slogan "Raised On Grit, Proven Through Storms" 32 years in Calgary
-Sale
-Page 1 & 2 design ideas
We are in your area, contact us today for your Exclusive limited time offer! *discounts apply exclusively to new agreements only
Updates
-Please keep simple, clean & bright
-I really like the bright blue from our new logo (new logo uploaded)
-We specialize in Roofing -Siding-Gutters & full Exterior Renos (like the competitor example uploaded)
-This is the NEW website we are currently working on (not finished) https://mockups.plenvio.net/view/8b2c4e71-d95a-4f0b-b7e3-c1c1c8823a7f-9d2b/?fullscreen
-This is our OLD website https://northpeakshinglepros.com
-For the sale "We are in your area, contact us today for your Exclusive limited time offer" *discounts apply exclusively to new agreements only
-Free Estimates
-our phone# is 403-555-0187
-our website is northpeakshinglepros.com
-keep simple, clean, bright use the "new logo" uploaded. Check out the competitor example uploaded file
-We are in your area, Contact us today for your Exclusive limited time offer! *discounts apply to new agreements only
-FREE ESTIMATES
-Specialized in Roofing /Siding /Gutters Full Exterior Reno's
-We are currently working on a NEW website https://mockups.plenvio.net/view/8b2c4e71-d95a-4f0b-b7e3-c1c1c8823a7f-9d2b/?fullscreen
-Our OLD website https://northpeakshinglepros.com/
-Post old site address on flyer northpeakshinglepros.com
-Phone # 403-555-0187
Target Market(s)
40-55
Industry/Entity Type
Roofing Siding & full Exterior Reno's
Look and feel

```html
<!DOCTYPE html>
<html lang="en">
<head>
<meta charset="utf-8">
<title>Korvell Roofing &amp; Siding – Door Hanger</title>
<link href="https://fonts.googleapis.com/css2?family=Open+Sans:wght@400;500&family=Montserrat:wght@500;600;700&family=Roboto:wght@400&display=swap" rel="stylesheet">
<style>
  :root {
    --blue: #1b66b3;
    --blue-mid: #3b86c8;
    --blue-dark: #1a5fae;
    --red: #ec1c24;
    --ink: #231f20;
    --swoosh: #e6e6e8;
    --dot: #e4e4f0;
    --white: #ffffff;
    --badge-plain: #e9ebef;
  }
  * { box-sizing: border-box; margin: 0; padding: 0; }
  html, body { width: 1092px; height: 1200px; overflow: hidden; background: var(--white); }
  .sheet { position: relative; width: 1092px; height: 1200px; }

  .side-label {
    position: absolute; top: 56px; width: 408px; text-align: center;
    font-family: "Open Sans", sans-serif; font-weight: 400; font-size: 58px;
    color: var(--blue); letter-spacing: -1px;
  }
  .side-label.front { left: 80px; }
  .side-label.back { left: 605px; }

  .hanger {
    position: absolute; width: 408px; height: 967px; background: var(--white);
    box-shadow: 14px 18px 28px rgba(0,0,0,0.35); overflow: hidden;
  }
  .hanger.front { left: 80px; top: 138px; }
  .hanger.back { left: 597px; top: 141px; }

  .hanger .decor { position: absolute; left: 0; top: 0; }

  .headline {
    position: absolute; top: 38px; left: 0; width: 100%; text-align: center;
    font-family: "Montserrat", sans-serif; font-weight: 700; font-size: 14px;
    letter-spacing: 2.4px; color: var(--blue);
  }

  .brand {
    position: absolute; left: 0; width: 100%; text-align: center;
    font-family: "Montserrat", sans-serif; font-weight: 600; color: var(--ink);
    line-height: 1.15;
  }
  .front .brand { top: 250px; }
  .back .brand { top: 254px; }
  .brand .brand-name { display: block; font-size: 34px; letter-spacing: 3px; }
  .brand .brand-trade { display: block; font-size: 15px; letter-spacing: 3.2px; margin-top: 4px; }

  .slogan {
    position: absolute; left: 0; width: 100%; text-align: center;
    font-family: "Roboto", sans-serif; font-size: 11.6px; color: var(--blue);
  }
  .front .slogan { top: 327px; }
  .back .slogan { top: 344px; }

  .service {
    position: absolute; left: 40px; width: 328px; height: 136px; border-radius: 18px;
    overflow: hidden; color: var(--white);
    font-family: "Montserrat", sans-serif;
  }
  .service .photo { position: absolute; inset: 0; }
  .service.roofing { top: 366px; }
  .service.roofing .photo { background: linear-gradient(135deg, #6b7689 0%, #7c8594 55%, #5a5450 100%); }
  .service.siding { top: 537px; }
  .service.siding .photo { background: linear-gradient(135deg, #7a7d86 0%, #8a8c92 55%, #6c6a66 100%); }
  .service.exteriors { top: 707px; }
  .service.exteriors .photo { background: linear-gradient(90deg, #6f6360 0%, #5c5b60 50%, #8d8670 52%, #6e6e6e 100%); }

  .service h2 {
    position: relative; text-align: center; font-weight: 700; font-size: 25px;
    letter-spacing: 4px; padding-top: 10px;
  }
  .service ul { position: relative; list-style: none; padding-left: 10px; margin-top: 2px; }
  .service li { font-weight: 500; font-size: 16px; letter-spacing: 1.8px; line-height: 20px; white-space: nowrap; }
  .service li::before { content: "\2756"; font-size: 12px; margin-right: 9px; vertical-align: 1px; }
  .roofing ul { margin-top: 6px; }
  .exteriors li { letter-spacing: 1.5px; }

  .contact {
    position: absolute; left: 0; width: 100%; text-align: center;
    font-family: "Montserrat", sans-serif; font-weight: 500; color: var(--blue);
    letter-spacing: 2px; line-height: 21px;
  }
  .front .contact, .back .contact { top: 868px; }
  .contact .contact-title { font-size: 20px; }
  .contact .contact-phone { font-size: 20px; }
  .contact .contact-web { font-size: 18px; }

  .footer-band { position: absolute; left: 0; bottom: 0; width: 100%; height: 24px; background: var(--red); }

  .about { position: absolute; left: 33px; top: 413px; font-family: "Montserrat", sans-serif; color: var(--blue); }
  .about h2 { font-weight: 700; font-size: 29px; letter-spacing: 3.5px; line-height: 34px; }
  .about ol { list-style: none; }
  .about li { font-size: 13.5px; font-weight: 500; letter-spacing: 1.8px; line-height: 17.5px; }

  .badge { position: absolute; background: var(--badge-plain); }
  .badge.alliance { left: 58px; top: 590px; width: 118px; height: 109px; }
  .badge.summit { left: 236px; top: 590px; width: 110px; height: 110px; border-radius: 50%; }
  .badge.council { left: 48px; top: 732px; width: 311px; height: 87px; border-radius: 14px; }
</style>
</head>
<body>
<main class="sheet">

  <h1 class="side-label front">FRONT</h1>
  <h1 class="side-label back">BACK SIDE</h1>

  <section class="hanger front">
    <svg class="decor" width="408" height="967" viewBox="0 0 408 967" aria-hidden="true">
      <path fill="var(--swoosh)" d="M0 100 C90 100 140 100 170 93 A46 46 0 1 1 170 157 C140 150 90 150 0 150 Z"/>
      <polygon fill="var(--blue-dark)" points="254,95 408,45 408,57 258,105"/>
      <polygon fill="var(--blue-mid)" points="260,108 408,66 408,78 262,122"/>
      <polygon fill="var(--red)" points="258,131 408,85 408,97 254,145"/>
      <g fill="var(--dot)">
        <circle cx="38" cy="165" r="6.5"/><circle cx="56" cy="165" r="6.5"/><circle cx="73" cy="165" r="6.5"/><circle cx="90" cy="165" r="6.5"/>
        <circle cx="56" cy="184" r="6.5"/><circle cx="73" cy="184" r="6.5"/><circle cx="91" cy="184" r="6.5"/><circle cx="108" cy="184" r="6.5"/>
        <circle cx="299" cy="165" r="6.5"/><circle cx="317" cy="165" r="6.5"/><circle cx="334" cy="165" r="6.5"/><circle cx="351" cy="165" r="6.5"/>
        <circle cx="317" cy="184" r="6.5"/><circle cx="334" cy="184" r="6.5"/><circle cx="352" cy="184" r="6.5"/><circle cx="369" cy="184" r="6.5"/>
      </g>
    </svg>

    <p class="headline">WE’RE IN YOUR NEIGHBOUR HOOD!</p>

    <div class="brand">
      <span class="brand-name">KORVELL</span>
      <span class="brand-trade">ROOFING &amp; SIDING</span>
    </div>

    <p class="slogan">Raised On Grit, Proven Through Storms” 32 Years In Calgary- Sale</p>

    <article class="service roofing">
      <div class="photo" role="img" aria-label="Photo of a house roof with dormers and asphalt shingles"></div>
      <h2>ROOFING</h2>
      <ul><li>Asphalt</li><li>Rubber</li><li>Metal</li></ul>
    </article>

    <article class="service siding">
      <div class="photo" role="img" aria-label="Photo of a two-storey house with new siding"></div>
      <h2>SIDING</h2>
      <ul><li>Premium fiber cement</li><li>Vinyl</li><li>Metal ( Steel, Aluminum )</li><li>Long-board</li></ul>
    </article>

    <article class="service exteriors">
      <div class="photo" role="img" aria-label="Photo collage of exterior renovation work"></div>
      <h2>FULL EXTERIORS</h2>
      <ul><li>Eaves trough / Soffit / Fascia</li><li>Stone</li><li>Skylights</li><li>Windows Doors</li></ul>
    </article>

    <div class="contact">
      <p class="contact-title">Contact with us:</p>
      <p class="contact-phone">+403-555-0187</p>
      <p class="contact-web">www.northpeakshinglepros.com</p>
    </div>

    <div class="footer-band"></div>
  </section>

  <section class="hanger back">
    <svg class="decor" width="408" height="967" viewBox="0 0 408 967" aria-hidden="true">
      <path fill="var(--swoosh)" transform="translate(408 0) scale(-1 1)" d="M0 100 C90 100 140 100 170 93 A46 46 0 1 1 170 157 C140 150 90 150 0 150 Z"/>
      <polygon fill="var(--red)" points="0,149 151,103 151,115 0,162"/>
      <polygon fill="var(--blue-mid)" points="0,167 153,125 153,137 0,182"/>
      <polygon fill="var(--blue-dark)" points="0,190 154,144 154,154 0,203"/>
      <g fill="var(--dot)">
        <circle cx="316" cy="186" r="6.5"/><circle cx="333" cy="186" r="6.5"/><circle cx="350" cy="186" r="6.5"/><circle cx="367" cy="186" r="6.5"/>
        <circle cx="298" cy="204" r="6.5"/><circle cx="315" cy="204" r="6.5"/><circle cx="332" cy="204" r="6.5"/><circle cx="349" cy="204" r="6.5"/>
      </g>
    </svg>

    <p class="headline">WE’RE IN YOUR NEIGHBOUR HOOD!</p>

    <div class="brand">
      <span class="brand-name">KORVELL</span>
      <span class="brand-trade">ROOFING &amp; SIDING</span>
    </div>

    <p class="slogan">Raised On Grit, Proven Through Storms” 32 Years In Calgary- Sale</p>

    <div class="about">
      <h2>About us:</h2>
      <ol>
        <li>1. 25 Year Labour warranty’s available</li>
        <li>2. 32 Years in Calgary</li>
        <li>3. QHT A+ Member</li>
      </ol>
    </div>

    <div class="badge alliance" role="img" aria-label="Contractor program badge"></div>
    <div class="badge summit" role="img" aria-label="Certified contractor badge"></div>
    <div class="badge council" role="img" aria-label="Roofing association membership badge"></div>

    <div class="contact">
      <p class="contact-title">Contact with us:</p>
      <p class="contact-phone">+403-555-0187</p>
      <p class="contact-web">www.northpeakshinglepros.com</p>
    </div>

    <div class="footer-band"></div>
  </section>

</main>
</body>
</html>
```